Wine Label Needed

We need a front and back wine label design for our new winery based out of Berks County, PA. We love designs using typography as a main element. We also need this done very quickly. I will have a higher resolution logo available to provide the winner with. The jpg attached labeled Vineyards is a stock image I purchased that can be included on the back of the label, possibly. Thanks so much!
Updates

Here are some additional inspirational ideas I came across: https://quillbazaar.net/TovrekSannel/41927-Drovik-Glyph-Set-62OFF https://quillbazaar.net/Perumbelle/38214-Lantern-Reef-Letterset-Bonus https://quillbazaar.net/odenvasko/27481-Quorvel-Typeface

I've uploaded the design board to our restaurant that we'll be selling the wine in so you can get an overall feel of the look of the business. Hope this helps!

Reason: Sorry for the extension, but I didn't plan this out very well since I leave for vacation Monday - Friday and need more time to look over all these fabulous submissions! Thanks for your understanding!

Just got back from vacation and will be looking over everyone's beautiful designs today! Thanks so much for your patience!

Target Market(s)

Younger crowd

Font styles to use
Serif
Decorative
Script

Requirements
Must have
• Must say 750 ml
Must have a vintage date listed of 2013
Use an example wine name, i.e. cabernet sauvignon
The back will have a description of the wine which I can provide at a later date and also the standard government warning. It will also need space for a bar code. The back must also say: Cellared and Bottled by Ravenmoor Estate Winery. Also must say: Contains Sulfites
Nice to have
• On the inspiration image attached for the can called Tidebrook, I love the typography that's used to describe the beverage. Could possibly do something like this, but we don't have descriptors of our wines just yet.

```html
<!DOCTYPE html>
<html lang="en">
<head>
<meta charset="utf-8">
<title>Ravenmoor Estate Winery – Cabernet Sauvignon 2013 Label</title>
<link rel="stylesheet" href="https://fonts.googleapis.com/css2?family=IM+Fell+Double+Pica&family=Pinyon+Script&family=Poiret+One&family=Playfair+Display:wght@400&display=swap">
<style>
  :root {
    --page-bg: #e9e6df;
    --label-white: #ffffff;
    --vine-green: #1f3d22;
    --vine-green-soft: #2c4f2e;
    --leaf-green: #8fb46a;
    --leaf-green-pale: #d9e6cc;
    --logo-brown: #4a3a22;
    --frame-line: #1f3d22;
  }
  * { margin: 0; padding: 0; box-sizing: border-box; }
  html, body {
    width: 1200px;
    height: 848px;
    overflow: hidden;
    background: var(--page-bg);
  }
  .canvas {
    position: relative;
    width: 1200px;
    height: 848px;
  }
  .label {
    position: absolute;
    left: 332px;
    top: 30px;
    width: 535px;
    height: 788px;
    background: var(--label-white);
    box-shadow: 0 4px 18px rgba(0,0,0,0.18);
  }
  .frame-line {
    position: absolute;
    border: 1px solid var(--frame-line);
    pointer-events: none;
  }
  .frame-line--outer { inset: 8px; }
  .frame-line--inner { inset: 13px; }

  .band {
    position: absolute;
    left: 24px;
    width: 487px;
  }
  .band--green { background: linear-gradient(180deg, var(--vine-green-soft), var(--vine-green)); }

  .band--crown    { top: 24px;  height: 88px; }
  .band--strip    { top: 124px; height: 30px; }
  .band--divider  { top: 420px; height: 29px; }
  .band--divider2 { top: 527px; height: 29px; }
  .band--base     { top: 650px; height: 114px; }

  .ornament { position: absolute; }
  .ornament--crown {
    left: 175px; top: 36px; width: 185px; height: 76px;
    background: radial-gradient(ellipse at 50% 90%, #ffffff 60%, #e7ece6 100%);
    border-radius: 50% 50% 0 0 / 80% 80% 0 0;
  }
  .ornament--vine {
    left: 140px; top: 188px; width: 255px; height: 40px;
    background: radial-gradient(ellipse at 50% 60%, var(--leaf-green) 0%, var(--leaf-green-pale) 70%, transparent 72%);
  }
  .ornament--flourish {
    left: 190px; top: 372px; width: 155px; height: 12px;
    background: radial-gradient(ellipse at 50% 50%, var(--vine-green-soft) 0%, var(--leaf-green-pale) 60%, transparent 70%);
  }
  .ornament--knot {
    left: 148px; top: 650px; width: 240px; height: 80px;
    background: radial-gradient(ellipse at 50% 20%, #ffffff 60%, #e3e9e2 100%);
    border-radius: 0 0 50% 50% / 0 0 100% 100%;
  }
  .ornament--leaf {
    top: 582px; width: 30px; height: 40px;
    background: var(--vine-green);
    border-radius: 50%;
  }
  .ornament--leaf-left  { left: 148px; }
  .ornament--leaf-right { left: 357px; }

  .brand {
    position: absolute;
    left: 24px;
    width: 487px;
    text-align: center;
    color: var(--logo-brown);
    font-family: "IM Fell Double Pica", Georgia, serif;
    font-weight: 400;
    line-height: 1;
  }
  .brand__name {
    top: 236px;
    font-size: 37px;
    letter-spacing: 1px;
  }
  .brand__descriptor {
    top: 292px;
    font-size: 14px;
    letter-spacing: 3px;
  }
  .motto {
    position: absolute;
    left: 24px;
    width: 487px;
    top: 318px;
    text-align: center;
    font-family: "Pinyon Script", cursive;
    font-size: 25px;
    line-height: 1.3;
    color: var(--vine-green);
  }
  .varietal {
    position: absolute;
    left: 24px;
    width: 487px;
    top: 449px;
    height: 78px;
    line-height: 78px;
    text-align: center;
    font-family: "Poiret One", sans-serif;
    font-weight: 400;
    font-size: 37px;
    letter-spacing: 2px;
    color: var(--vine-green);
  }
  .vintage {
    position: absolute;
    left: 24px;
    width: 487px;
    top: 560px;
    text-align: center;
    font-family: "Playfair Display", Georgia, serif;
    font-size: 72px;
    line-height: 1;
    color: var(--vine-green);
  }
  .volume {
    position: absolute;
    right: 34px;
    top: 710px;
    font-family: "Playfair Display", Georgia, serif;
    font-size: 31px;
    line-height: 1;
    color: var(--label-white);
  }
</style>
</head>
<body>
  <main class="canvas">
    <article class="label" aria-label="Front wine label">
      <div class="frame-line frame-line--outer"></div>
      <div class="frame-line frame-line--inner"></div>

      <div class="band band--green band--crown"></div>
      <div class="band band--green band--strip"></div>
      <div class="band band--green band--divider"></div>
      <div class="band band--green band--divider2"></div>
      <div class="band band--green band--base"></div>

      <div class="ornament ornament--crown" role="img" aria-label="Decorative white scrollwork crest at the top of the label"></div>
      <div class="ornament ornament--vine" role="img" aria-label="Grapevine and scroll ornament above the winery name"></div>

      <p class="brand brand__name">RAVENMOOR ESTATE</p>
      <p class="brand brand__descriptor">WINERY</p>
      <p class="motto">Nel Vino C'è la Verità</p>
      <div class="ornament ornament--flourish" role="img" aria-label="Small scroll flourish"></div>

      <h1 class="varietal">CABERNET SAUVIGNON</h1>

      <div class="ornament ornament--leaf ornament--leaf-left" role="img" aria-label="Small leaf ornament"></div>
      <p class="vintage">2013</p>
      <div class="ornament ornament--leaf ornament--leaf-right" role="img" aria-label="Small leaf ornament"></div>

      <div class="ornament ornament--knot" role="img" aria-label="Decorative white interlaced flourish below the vintage"></div>

      <p class="volume">750 ml</p>
    </article>
  </main>
</body>
</html>
```